Business card design for upmarket Home Technology design and Installation company

Hello designers, we need a great business card designed.
We need it to convey high tech, and also sophistication .
We work with some of the most affluent people in the world building them home technology systems, and A/V entertainment systems.

Services offered include the following:
Design, sales, installation, and maintenance of

*Home Automation systems
*Distributed / Multi-Room Audio and Video
*High Performance Networks & WiFi
* Lighting and Shade Control
*Home cinema
*Security and CCTV Systems

I have included a copy of our logo to use for your design efforts.

Target Market(s)

Upmarket clients with multi million euro villas.

Industry/Entity Type

Home technology

Contact Information for Business Card

NAME: Derek Halloran ADDRESS: Plaza Brisa Local 42, Port Andratx, 07392 PHONE: +34-602-518-794 EMAIL: DHalloran@VELTRAsmarthomes.com WEB: www.veltrasmarthomes.com

Requirements
Must have
• Our Logo, and our tagline

```html
<!DOCTYPE html>
<html lang="en">
<head>
<meta charset="utf-8">
<title>VELTRA Smarter Homes – Business Card</title>
<link rel="stylesheet" href="https://fonts.googleapis.com/css2?family=Nunito:wght@300;400;600;700;800&display=swap">
<style>
  :root {
    --backdrop: #2b2e34;
    --card: #050505;
    --gold: #cfa53e;
    --gold-light: #f3d77a;
    --gold-dark: #9c7424;
    --ink: #ffffff;
    --stripe: linear-gradient(90deg, var(--gold-dark) 0%, var(--gold-light) 45%, var(--gold) 70%, var(--gold-dark) 100%);
  }
  * { box-sizing: border-box; margin: 0; padding: 0; }
  html, body {
    width: 1200px; height: 780px; overflow: hidden;
    background: var(--backdrop);
    font-family: "Nunito", sans-serif;
  }
  .stage {
    width: 1200px; height: 780px;
    display: flex; align-items: center; justify-content: center; gap: 40px;
  }
  .card {
    position: relative;
    width: 540px; height: 310px;
    background: var(--card);
    border-radius: 22px;
    overflow: hidden;
    color: var(--ink);
    box-shadow: 0 18px 40px rgba(0,0,0,.45);
  }
  .wordmark {
    position: absolute;
    color: var(--gold);
    font-weight: 400;
    letter-spacing: 6px;
    line-height: 1;
  }
  .wordmark__name { font-size: 62px; display: flex; align-items: center; gap: 14px; }
  .wordmark__dot { width: 16px; height: 16px; border-radius: 50%; background: var(--gold); }
  .wordmark__tagline { font-size: 30px; letter-spacing: 1px; margin-top: 6px; padding-left: 4px; }
  .gold-stripe {
    position: absolute; left: 0; right: 0; height: 7px;
    background: var(--stripe);
  }

  /* front */
  .card--front .wordmark { top: 30px; left: 34px; }
  .card--front .gold-stripe { bottom: 24px; }
  .contact-list {
    position: absolute; left: 26px; bottom: 44px;
    list-style: none; font-size: 12.5px; font-weight: 600; line-height: 1.6;
    white-space: nowrap;
  }
  .contact-list li { display: flex; align-items: center; gap: 8px; }
  .contact-list svg { width: 11px; height: 11px; flex: none; }
  .person {
    position: absolute; right: 26px; bottom: 48px; text-align: left;
    white-space: nowrap;
  }
  .person__name { font-size: 28px; font-weight: 800; line-height: 1; }
  .person__role { font-size: 17px; font-weight: 300; color: var(--gold); margin-top: 4px; letter-spacing: 0.5px; }

  /* back */
  .card--back .wordmark { top: 26px; right: 34px; text-align: right; }
  .card--back .wordmark__name { justify-content: flex-end; }
  .card--back .gold-stripe { top: 152px; }
  .services {
    position: absolute; left: 30px; right: 30px; top: 170px; text-align: center;
  }
  .services__title { font-size: 17px; font-weight: 700; letter-spacing: 5px; }
  .services__lead { font-size: 16px; font-weight: 700; margin-top: 2px; }
  .services__columns {
    display: flex; justify-content: space-between; text-align: left;
    margin-top: 8px; font-size: 12.5px; font-weight: 600; line-height: 1.5;
  }
  .services__columns ul { list-style: none; }
  .services__columns li::before { content: "▪"; margin-right: 6px; }
</style>
</head>
<body>
<main class="stage">
  <article class="card card--front">
    <div class="wordmark">
      <div class="wordmark__name">VELTRA <span class="wordmark__dot"></span></div>
      <div class="wordmark__tagline">Smarter Homes</div>
    </div>
    <ul class="contact-list">
      <li>
        <svg viewBox="0 0 12 12"><path fill="var(--gold)" d="M2.5 1 4.6 3.1 3.6 4.3a7 7 0 0 0 4.1 4.1l1.2-1L11 9.5 9.6 11C5 10.6 1.4 7 1 2.4z"/></svg>
        +34-602-518-794
      </li>
      <li>
        <svg viewBox="0 0 12 12"><rect x="1" y="2.5" width="10" height="7" rx="1" fill="var(--gold)"/><path d="M1.5 3 6 6.5 10.5 3" stroke="#050505" fill="none"/></svg>
        DHalloran@VELTRAsmarthomes.com
      </li>
      <li>
        <svg viewBox="0 0 12 12"><g fill="none" stroke="var(--gold)" stroke-width="1.2"><circle cx="6" cy="6" r="5"/><ellipse cx="6" cy="6" rx="2.2" ry="5"/><path d="M1 6h10"/></g></svg>
        www.veltrasmarthomes.com
      </li>
      <li>
        <svg viewBox="0 0 12 12"><path fill="var(--gold)" d="M6 .8a4 4 0 0 0-4 4C2 8 6 11.4 6 11.4S10 8 10 4.8a4 4 0 0 0-4-4zm0 5.6a1.6 1.6 0 1 1 0-3.2 1.6 1.6 0 0 1 0 3.2z"/></svg>
        Plaza Brisa Local 42, Port Andratx, 07392
      </li>
    </ul>
    <div class="person">
      <div class="person__name">Derek Halloran</div>
      <div class="person__role">FOUNDER/CEO</div>
    </div>
    <div class="gold-stripe"></div>
  </article>

  <article class="card card--back">
    <div class="wordmark">
      <div class="wordmark__name">VELTRA <span class="wordmark__dot"></span></div>
      <div class="wordmark__tagline">Smarter Homes</div>
    </div>
    <div class="gold-stripe"></div>
    <section class="services">
      <h2 class="services__title">SERVICES</h2>
      <p class="services__lead">Design, Sales, Installation &amp; Maintenance of</p>
      <div class="services__columns">
        <ul>
          <li>Home Automation systems</li>
          <li>Distributed Multi-Room Audio &amp; Video</li>
          <li>High Performance Networks &amp; WiFi</li>
        </ul>
        <ul>
          <li>Lighting and Shade Control</li>
          <li>Home cinema</li>
          <li>Security and CCTV Systems</li>
        </ul>
      </div>
    </section>
  </article>
</main>
</body>
</html>
```